Website Refresh for Niche Pet Website

We have a site that needs a fresh, modern look. This site gets approx 500K views a month and we want a re-design.

Category layout
New blog template layout

We need to keep the large rolling ads on the home page
The small ad need to be placed on the side when looking at the interior page.

We need a modern slick easy to use site

Target Market(s)

Breeders and pet buyers in the UK

Industry/Entity Type

pets

Number of Pages Required

4 page

Requirements
Must have
• Be Gun Dog specific - these are for working homes. Creative way to showcase the ads, breeds etc.
Nice to have
• We are open to logo improvements and colour, however, this is the UK market for buying and selling gun dogs. The grren and gold do work well.

```html
<!DOCTYPE html>
<html lang="en">
<head>
<meta charset="utf-8">
<title>Field Hound Exchange</title>
<link rel="stylesheet" href="https://fonts.googleapis.com/css2?family=Bebas+Neue&family=Work+Sans:wght@400;500;600&display=swap">
<style>
:root{
  --green:#485c2b;
  --green-dark:#34441d;
  --gold:#c9a15b;
  --grey:#f4f4f4;
  --ink:#222;
  --muted:#555;
  --white:#fff;
  --black:#000;
}
*{box-sizing:border-box;margin:0;padding:0}
html,body{width:1200px;height:4762px;overflow:hidden}
body{position:relative;background:var(--white);font-family:"Work Sans",sans-serif;color:var(--ink)}
.abs{position:absolute}
.display{font-family:"Bebas Neue",sans-serif;letter-spacing:.5px}
.btn{position:absolute;display:flex;align-items:center;justify-content:center;font-family:"Bebas Neue",sans-serif;color:var(--white);background:var(--green);font-size:17px;letter-spacing:.5px}
.btn.round{border-radius:24px}
.btn.square{border-radius:5px}

/* header */
.site-header{top:0;left:0;width:1200px;height:84px;background:var(--white)}
.brand{display:flex;align-items:center;gap:14px}
.brand-dot{width:60px;height:60px;border-radius:50%;background:#ececec}
.brand-name{font-family:"Bebas Neue",sans-serif;font-size:30px;color:var(--ink)}
.nav{top:30px;left:558px;display:flex;gap:24px;font-size:14px;color:#333}
.menu-icon{top:33px;left:882px;width:14px}
.menu-icon span{display:block;height:2px;background:#333;margin-bottom:3px}

/* hero */
.hero{top:84px;left:0;width:1200px;height:621px;overflow:hidden;background:linear-gradient(180deg,#aeb2ad 0%,#8d8c7e 45%,#6b5b3f 75%,#4c3f2a 100%)}
.hero-disc{left:290px;top:26px;width:620px;height:620px;border-radius:50%;background:#38481f}
.hero-title{top:112px;left:0;width:1200px;text-align:center;font-size:118px;color:var(--white);line-height:1}
.hero-title em{font-style:normal;color:var(--gold)}
.search-card{top:271px;left:268px;width:664px;height:193px;background:var(--white);border-radius:10px}
.search-card h2{position:absolute;top:36px;width:100%;text-align:center;font-size:26px;font-weight:400}
.search-card label{position:absolute;top:70px;left:55px;font-size:13px;font-weight:500}
.select{position:absolute;top:92px;left:43px;width:438px;height:52px;background:#ececec;border-radius:6px;font-size:14px;color:#444;padding:17px 22px}
.select::after{content:"";position:absolute;right:24px;top:23px;border:5px solid transparent;border-top-color:#222}
.search-btn{top:92px;left:504px;width:120px;height:50px;background:var(--gold);border-radius:6px;font-size:20px}

/* categories */
.section-title{left:0;width:1200px;text-align:center;font-size:42px;font-weight:400}
.cat{width:200px;text-align:center}
.cat-ring{width:172px;height:172px;border-radius:50%;background:var(--white);box-shadow:0 4px 14px rgba(0,0,0,.12);margin:0 auto;padding:8px}
.cat-ring div{width:156px;height:156px;border-radius:50%;background:var(--green)}
.cat h3{font-family:"Bebas Neue",sans-serif;font-weight:400;font-size:28px;margin-top:18px}
.cat a{font-family:"Bebas Neue",sans-serif;font-size:13px;color:var(--gold)}
.arrow{width:28px;height:28px;border-radius:50%;display:flex;align-items:center;justify-content:center;font-size:14px;color:#fff}

/* welcome */
.welcome-band{top:1305px;left:0;width:1200px;height:680px;background:var(--grey)}
.welcome-photo{left:113px;top:1388px;width:414px;height:406px;border-radius:50%;background:radial-gradient(circle at 45% 45%,#5a4a30,#6f8a3a 60%,#4f6a2a)}
.copy{font-size:14.5px;line-height:28px;color:#333}

/* listings */
.listing{width:306px;text-align:center}
.listing-img{height:294px;border-radius:18px}
.listing h3{font-family:"Bebas Neue",sans-serif;font-weight:400;font-size:30px;margin-top:26px}
.listing p{font-size:14px;line-height:23px}
.listing .price{font-family:"Bebas Neue",sans-serif;font-size:26px;color:var(--green);margin-top:10px}

/* feature boxes */
.feature{background:var(--white);box-shadow:0 2px 16px rgba(0,0,0,.1)}
.feature h2{font-family:"Bebas Neue",sans-serif;font-weight:400;font-size:38px}

/* contact */
.field{height:50px;background:var(--white);box-shadow:0 2px 10px rgba(0,0,0,.1);font-size:14px;color:#555;padding:16px 20px;display:flex;gap:8px;align-items:flex-start}
.partner{width:198px;height:198px;border-radius:14px;box-shadow:0 2px 12px rgba(0,0,0,.15);background:var(--white);padding:6px}
.partner div{width:100%;height:100%;border-radius:10px}

/* footer */
.site-footer{top:4328px;left:0;width:1200px;height:434px;background:var(--black);color:var(--white)}
.footer-links{top:215px;width:1200px;display:flex;justify-content:center;gap:26px;font-size:15px}
.copyright{top:272px;width:1200px;text-align:center;font-size:13px}
.social{top:314px;width:44px;height:44px;border-radius:50%}
</style>
</head>
<body>

<header class="site-header abs">
  <div class="brand abs" style="left:120px;top:12px">
    <span class="brand-dot"></span><span class="brand-name">Field Hound Exchange</span>
  </div>
  <nav class="nav abs"><span>Lost/Stolen Dogs</span><span>Events</span><span>Information</span></nav>
  <div class="menu-icon abs"><span></span><span></span><span></span></div>
  <a class="btn square" style="left:925px;top:23px;width:126px;height:38px;border-radius:2px;font-size:15px">Place Advert</a>
</header>

<section class="hero abs" role="img" aria-label="Hunter in camouflage holding a gun in tall reeds with a retriever dog">
  <div class="hero-disc abs"></div>
  <h1 class="hero-title abs display" style="font-weight:400">Field <em>Hound</em> Exchange</h1>
  <form class="search-card abs">
    <h2 class="display">Find a Gundog</h2>
    <label>LOCATION</label>
    <div class="select">Select County</div>
    <div class="btn search-btn">Search</div>
  </form>
</section>

<h2 class="section-title abs display" style="top:782px">Our Categories</h2>
<div class="arrow abs" style="left:42px;top:963px;background:#ccc">&lsaquo;</div>
<div class="arrow abs" style="left:1127px;top:963px;background:var(--gold)">&rsaquo;</div>
<div class="cat abs" style="left:87px;top:879px"><div class="cat-ring"><div role="img" aria-label="Labrador icon"></div></div><h3>Labradors</h3><a>Learn More</a></div>
<div class="cat abs" style="left:293px;top:879px"><div class="cat-ring"><div role="img" aria-label="Springer spaniel icon"></div></div><h3>Springer Spaniels</h3><a>Learn More</a></div>
<div class="cat abs" style="left:498px;top:879px"><div class="cat-ring"><div role="img" aria-label="Cocker spaniel icon"></div></div><h3>Cocker Spaniels</h3><a>Learn More</a></div>
<div class="cat abs" style="left:704px;top:879px"><div class="cat-ring"><div role="img" aria-label="Lost dog icon"></div></div><h3>Lost/Stolen Dogs</h3><a>Learn More</a></div>
<div class="cat abs" style="left:909px;top:879px"><div class="cat-ring"><div role="img" aria-label="Events calendar icon"></div></div><h3>Events &amp; Trials</h3><a>Learn More</a></div>

<section class="welcome-band abs"></section>
<div class="welcome-photo abs" role="img" aria-label="Black labrador retrieving a pheasant on grass"></div>
<h2 class="abs display" style="left:590px;top:1372px;font-size:46px;font-weight:400">Welcome to Field Hound Exchange</h2>
<p class="copy abs" style="left:591px;top:1440px;width:480px">Our aim at FieldHoundExchange has always been to provide the very best gundog advertisement platform to purchase and sell your gundogs in the safest possible way. FieldHoundExchange was created by gundog people that know your time is valuable and best spent in the field with your dogs, thats why we have no lengthy registration forms to fill in or no accounts to remember passwords for adverts you posted 3 months ago.</p>
<p class="copy abs" style="left:591px;top:1646px;width:480px">Here at FieldHoundExchange your advert stays on until sold and all we ask in return is that you keep your advert</p>
<a class="btn round" style="left:588px;top:1720px;width:135px;height:46px">Learn More</a>

<div class="listing abs" style="left:112px;top:1901px">
  <div class="listing-img" role="img" aria-label="Fox red labrador nursing puppies" style="background:linear-gradient(135deg,#b78a5c,#d8b08a 50%,#9a7a66)"></div>
  <h3>Puppies</h3><p>Chatteris, Cambridgeshire<br>7th October 2023</p><div class="price">$1095.00</div>
</div>
<div class="listing abs" style="left:448px;top:1901px">
  <div class="listing-img" role="img" aria-label="Litter of puppies" style="background:#b18c4c;position:relative"><span class="btn round" style="left:88px;top:125px;width:132px;height:44px">Learn More</span></div>
  <h3>Puppies</h3><p>Whitby, North Yorkshire<br>7th October 2023</p><div class="price">$1000.00</div>
</div>
<div class="listing abs" style="left:784px;top:1901px">
  <div class="listing-img" role="img" aria-label="Spaniel puppy sitting on paving" style="background:linear-gradient(180deg,#c9bfb2,#a89888 60%,#8f8378)"></div>
  <h3>Puppies</h3><p>Southnormanton, Derbyshire<br>7th October 2023</p><div class="price">$1200.00</div>
</div>

<section class="feature abs" style="left:112px;top:2448px;width:975px;height:428px">
  <div class="abs" role="img" aria-label="Spaniel leaping over a log in woodland" style="left:12px;top:12px;width:324px;height:404px;background:linear-gradient(160deg,#7b8a4a,#9a6a3a 50%,#55602c)"></div>
  <h2 class="abs" style="left:375px;top:52px">FieldHoundExchange Safe Deposit Service</h2>
  <p class="copy abs" style="left:376px;top:106px;width:540px;font-size:14px">Your safety is our number one priority when purchasing a gun dog and we have teamed up with SafeHold to have tailor made a gundog escrow just for YOU, so now you can pay deposits for gun dogs safely without the fear of being scammed and losing deposits for your new gun dog. We have made the FieldHoundExchange Safe Deposit Service FREE for all breeders to use so there is really no good reason not to support the service and help keep the buyers safe when they part with large sums of money.</p>
  <a class="btn square" style="left:375px;top:330px;width:125px;height:42px;font-size:14px">Learn More</a>
</section>

<section class="feature abs" style="left:102px;top:2948px;width:978px;height:429px">
  <h2 class="abs" style="left:63px;top:52px">Buy, Sell &amp; Connect</h2>
  <p class="copy abs" style="left:64px;top:106px;width:540px;font-size:14px;line-height:30px">When you post an advert with FieldHoundExchange you will be sent a email confirmation (check spam folder) on that email you will find an edit link that allows you to edit your gundog advert when you like, we advice you keep the email safe for future use. If you post an advert we ask that you keep them up to date at all times. When you sell your gundog you can edit your own advert and mark the dog has sold.</p>
  <a class="btn square" style="left:63px;top:330px;width:125px;height:42px;font-size:14px">Learn More</a>
  <div class="abs" role="img" aria-label="Three labradors and a spaniel sitting beside a gun slip and pheasant" style="left:637px;top:14px;width:326px;height:402px;background:linear-gradient(180deg,#6d7a3e,#3d3a2a 55%,#7a5a3a)"></div>
</section>

<h2 class="section-title abs display" style="top:3468px;font-size:36px">Contact Us</h2>
<p class="abs" style="top:3518px;left:300px;width:600px;text-align:center;font-size:14.5px;line-height:24px;color:#333">Lorem ipsum dolor sit amet, consectetur adipiscing elit, sed do eiusmod tempor incididunt ut labore et dolore magna aliqua.</p>
<div class="field abs" style="left:112px;top:3605px;width:312px"><svg width="14" height="14" viewBox="0 0 14 14" fill="none" stroke="#555"><circle cx="7" cy="4.5" r="3"/><path d="M1.5 13c0-3 2.5-5 5.5-5s5.5 2 5.5 5"/></svg>Name</div>
<div class="field abs" style="left:442px;top:3605px;width:314px"><svg width="14" height="14" viewBox="0 0 14 14" fill="none" stroke="#555"><rect x="1" y="3" width="12" height="8"/><path d="M1 3l6 5 6-5"/></svg>Email</div>
<div class="field abs" style="left:773px;top:3605px;width:315px"><svg width="14" height="14" viewBox="0 0 14 14" fill="none" stroke="#555"><path d="M3 1l2 3-1.5 1.5c1 2 3 4 5 5L10 9l3 2-1.5 2C6 13 1 8 1 2.5z"/></svg>Phone</div>
<div class="field abs" style="left:112px;top:3675px;width:976px;height:170px"><svg width="14" height="14" viewBox="0 0 14 14" fill="none" stroke="#555"><path d="M2 2h10v7H6l-3 3V9H2z"/></svg>Comments</div>
<a class="btn square" style="left:538px;top:3875px;width:133px;height:46px;font-size:15px">Submit</a>

<div class="partner abs" style="left:170px;top:4032px"><div role="img" aria-label="Partner badge" style="background:#e9edf3"></div></div>
<div class="partner abs" style="left:390px;top:4032px"><div role="img" aria-label="Partner badge" style="background:linear-gradient(180deg,#c9a35a,#6a4a2a)"></div></div>
<div class="partner abs" style="left:610px;top:4032px"><div role="img" aria-label="Partner badge" style="background:#f1f1f1"></div></div>
<div class="partner abs" style="left:829px;top:4032px"><div role="img" aria-label="Partner badge" style="background:linear-gradient(135deg,#5a2a5a,#6b5a3a)"></div></div>

<footer class="site-footer abs">
  <div class="brand abs" style="left:472px;top:100px">
    <span class="brand-dot" style="width:70px;height:70px;background:#ddd"></span><span class="brand-name" style="color:var(--white);font-size:30px">Field Hound Exchange</span>
  </div>
  <nav class="footer-links abs"><span>Home</span><span>Information</span><span>Buyer Deposit Service</span><span>Contact Us</span></nav>
  <p class="copyright abs">Copyright Field Hound Exchange 2023. Site by Northgate Web Terms &amp; Conditions Privacy Policy</p>
  <span class="social abs" style="left:546px;background:var(--gold)"></span>
  <span class="social abs" style="left:598px;background:var(--white)"></span>
</footer>

</body>
</html>
```